Cedar Harbor Business Cards For New Startup

I am looking for you to design some business cards for a new startup https://cedarharborhub.com. I have supplied logo, brand guidelines and our signatures as a guide.

We need this to reflect the brand guidelines and the website for brand consistency,

What is Cedar Harbor?

Mallorca's Business Growth Community
Join your new business community full of passionate entrepreneurs who
love to solve problems and help each other grow together!

Any questions you can ask.

Target Market(s)

Business to Business

Contact Information for Business Card

These are attached (signatures) to the job

Font styles to use
Other font styles liked:
• Open Sans

Requirements
Must have
• Match design guidelines
Nice to have
• Photos of our faces so people remember us

```html
<!DOCTYPE html>
<html lang="en">
<head>
<meta charset="utf-8">
<title>Cedar Harbor – Business Cards</title>
<link href="https://fonts.googleapis.com/css2?family=Open+Sans:wght@400;700&display=swap" rel="stylesheet">
<style>
  :root {
    --olive: #5f6400;
    --olive-dark: #4f5300;
    --olive-light: #6f7410;
    --band-line: #d9cfa8;
    --paper: #ffffff;
    --paper-shade: #f1f1f1;
    --ink-grey: #4a4a4a;
    --stage: #3a3b3d;
  }
  html, body {
    margin: 0;
    padding: 0;
    width: 1200px;
    height: 1000px;
    overflow: hidden;
    background: var(--stage);
    font-family: "Open Sans", Arial, sans-serif;
  }
  .canvas {
    position: relative;
    width: 1200px;
    height: 1000px;
  }
  .card {
    position: absolute;
    left: 250px;
    width: 700px;
    height: 400px;
    overflow: hidden;
    box-shadow: 0 10px 30px rgba(0,0,0,0.45);
  }

  /* Back of card */
  .card-back {
    top: 60px;
    background: linear-gradient(135deg, var(--olive-light), var(--olive-dark));
    color: var(--paper);
  }
  .social-row {
    position: absolute;
    top: 22px;
    right: 26px;
    display: flex;
    gap: 6px;
  }
  .social-square {
    width: 22px;
    height: 22px;
    background: var(--paper);
    border-radius: 2px;
  }
  .back-brand {
    position: absolute;
    top: 50%;
    left: 50%;
    transform: translate(-50%, -58%);
    display: flex;
    align-items: center;
    gap: 16px;
    white-space: nowrap;
  }
  .back-brand .brand-dot {
    width: 44px;
    height: 44px;
    border: 4px solid var(--paper);
    border-radius: 50%;
    box-sizing: border-box;
  }
  .back-brand .brand-name {
    font-size: 44px;
    font-weight: 400;
    color: var(--paper);
  }
  .back-url {
    position: absolute;
    bottom: 34px;
    width: 100%;
    text-align: center;
    font-size: 22px;
    letter-spacing: 6px;
    color: var(--paper);
  }

  /* Front of card */
  .card-front {
    top: 530px;
    background: linear-gradient(160deg, var(--paper) 40%, var(--paper-shade));
  }
  .front-brand {
    position: absolute;
    left: 40px;
    top: 118px;
    width: 260px;
    display: flex;
    align-items: center;
    gap: 12px;
  }
  .front-brand .brand-dot {
    width: 34px;
    height: 34px;
    border: 4px solid var(--olive);
    border-radius: 50%;
    box-sizing: border-box;
    flex: none;
  }
  .front-brand .brand-name {
    font-size: 30px;
    font-weight: 400;
    color: var(--olive);
    white-space: nowrap;
  }
  .divider {
    position: absolute;
    left: 322px;
    top: 50px;
    width: 2px;
    height: 210px;
    background: linear-gradient(to bottom, rgba(0,0,0,0), #8a8a8a 50%, rgba(0,0,0,0));
  }
  .contact-block {
    position: absolute;
    left: 352px;
    top: 52px;
  }
  .person-name {
    margin: 0;
    font-size: 30px;
    font-weight: 700;
    color: var(--olive);
    letter-spacing: 0.5px;
    line-height: 1.1;
    white-space: nowrap;
  }
  .person-role, .person-company {
    margin: 2px 0 0;
    font-size: 19px;
    color: var(--olive);
    line-height: 1.2;
  }
  .contact-list {
    list-style: none;
    margin: 18px 0 0;
    padding: 0;
  }
  .contact-list li {
    display: flex;
    align-items: center;
    gap: 12px;
    font-size: 19px;
    color: var(--ink-grey);
    line-height: 1.35;
    white-space: nowrap;
  }
  .contact-list svg {
    width: 16px;
    height: 16px;
    flex: none;
  }
  .front-band {
    position: absolute;
    left: 0;
    bottom: 0;
    width: 100%;
    height: 72px;
    background: var(--olive);
  }
  .front-band::before {
    content: "";
    position: absolute;
    left: 0;
    top: 8px;
    width: 100%;
    height: 3px;
    background: var(--band-line);
  }
</style>
</head>
<body>
<main class="canvas">

  <section class="card card-back" aria-label="Business card back">
    <div class="social-row" aria-label="Social profiles">
      <span class="social-square"></span>
      <span class="social-square"></span>
      <span class="social-square"></span>
      <span class="social-square"></span>
      <span class="social-square"></span>
    </div>
    <div class="back-brand">
      <span class="brand-dot"></span>
      <span class="brand-name">Cedar Harbor</span>
    </div>
    <div class="back-url">cedarharborhub.com</div>
  </section>

  <section class="card card-front" aria-label="Business card front">
    <div class="front-brand">
      <span class="brand-dot"></span>
      <span class="brand-name">Cedar Harbor</span>
    </div>
    <div class="divider"></div>
    <div class="contact-block">
      <h1 class="person-name">TOBREN VASKELL</h1>
      <p class="person-role">Founder &amp; Growth Hacker</p>
      <p class="person-company">Cedar Harbor</p>
      <ul class="contact-list">
        <li>
          <svg viewBox="0 0 16 16" aria-hidden="true"><rect x="3.5" y="1" width="9" height="14" rx="1.5" fill="none" stroke="#5f6400" stroke-width="1.8"/><rect x="6.5" y="12" width="3" height="1.4" fill="#5f6400"/></svg>
          <span>+34 600 555 018</span>
        </li>
        <li>
          <svg viewBox="0 0 16 16" aria-hidden="true"><rect x="1" y="3" width="14" height="10" fill="#5f6400"/><path d="M1 3 L8 9 L15 3" fill="none" stroke="#fff" stroke-width="1.3"/></svg>
          <span>tv@cedarharborhub.com</span>
        </li>
        <li>
          <svg viewBox="0 0 16 16" aria-hidden="true"><circle cx="8" cy="8" r="7" fill="#5f6400"/><ellipse cx="8" cy="8" rx="3" ry="7" fill="none" stroke="#fff" stroke-width="1"/><line x1="1" y1="8" x2="15" y2="8" stroke="#fff" stroke-width="1"/></svg>
          <span>www.cedarharborhub.com</span>
        </li>
      </ul>
    </div>
    <div class="front-band"></div>
  </section>

</main>
</body>
</html>
```